Business card for Eyelash extension salon in Beverly Hills,California USA

We need new business card for our salon in Beverly Hills. The salon name is 'Lumarra' . We would like to have...Business name: Lumarra Name of person: will provide later Address 6128 N.Corbel Ridge Blvd Beverly Hills , CA 90210 Phone: will provide later (Text only) Web: www.lumarrastudio-example.com Pictogrid icon, Friendvale icon follow us for seasonal campaign and news @lumarrastudioexample Design should look elegant, high-end, clean, simple, cohesive with my brand. Please refer my brand board. Business name color will be metallic bronzy color. Im thinking grey background or white background. Thanks

Target Market(s)

25-35. Gender neutral. People who are in Entertainment business industry.
This is High-end Eyelash extension salon in Beverly Hills

Industry/Entity Type

Beauty Salon

Contact Information for Business Card

Business name: Lumarra
Name of person: will provide later
Address 6128 N.Corbel Ridge Blvd Beverly Hills , CA 90210
Phone: will provide later (Text only)
Web: www.lumarrastudio-example.com
Pictogrid icon, Friendvale icon
follow us for seasonal campaign and news @lumarrastudioexample

Requirements
Must have
• Beautiful, elegant, clean and simple look but very attractive and modern
Should not have
• We don't like too clutter, too busy designs.

```html
<!DOCTYPE html>
<html lang="en">
<head>
<meta charset="utf-8">
<title>Lumarra Business Card</title>
<link href="https://fonts.googleapis.com/css2?family=Bodoni+Moda:wght@400;500;700&family=Josefin+Sans:wght@400&display=swap" rel="stylesheet">
<style>
  :root {
    --page: #ffffff;
    --card: #f2f2f2;
    --bronze: #a8895a;
    --bronze-deep: #9c7e4e;
    --gold-light: #e9cd7e;
    --bronze-soft: #b99b6c;
    --bronze-tint: #dccfb8;
    --ink: #1a1a1a;
  }
  * { margin: 0; padding: 0; box-sizing: border-box; }
  html, body {
    width: 1200px; height: 1000px; overflow: hidden;
    background: var(--page);
  }
  .canvas { position: relative; width: 1200px; height: 1000px; }
  .card {
    position: absolute; top: 83px; width: 500px; height: 834px;
    background: var(--card);
  }
  .card--front { left: 75px; }
  .card--back { left: 625px; }

  /* Front */
  .eye-illustration {
    position: absolute; left: 270px; top: 130px; width: 230px; height: 294px;
    background: linear-gradient(160deg, var(--bronze-tint), #e6ddcd);
  }
  .front-wordmark {
    position: absolute; left: 0; top: 560px; width: 500px; text-align: center;
    font-family: "Bodoni Moda", serif; font-weight: 400; font-size: 104px;
    color: var(--bronze); letter-spacing: 2px; line-height: 1;
  }
  .front-locale {
    position: absolute; left: 244px; top: 709px;
    font-family: "Josefin Sans", sans-serif; font-size: 15px; letter-spacing: 3px;
    color: var(--bronze);
  }
  .front-tagline {
    position: absolute; left: 0; top: 768px; width: 500px; text-align: center;
    font-family: "Bodoni Moda", serif; font-weight: 700; font-size: 21px;
    letter-spacing: 2.2px; color: var(--bronze);
  }

  /* Back */
  .back-wordmark {
    position: absolute; left: 0; top: 52px; width: 500px; text-align: center;
    font-family: "Bodoni Moda", serif; font-weight: 400; font-size: 50px;
    color: var(--bronze); line-height: 1;
  }
  .back-locale {
    position: absolute; left: 222px; top: 130px;
    font-family: "Josefin Sans", sans-serif; font-size: 7px; letter-spacing: 1.5px;
    color: var(--bronze);
  }
  .contact-list { position: absolute; left: 0; top: 160px; width: 500px; list-style: none; }
  .contact-item {
    position: absolute; left: 0; height: 20px; display: flex; align-items: center;
    font-family: "Bodoni Moda", serif; font-size: 12px; letter-spacing: 1.6px; color: var(--ink);
  }
  .contact-item::before {
    content: ""; width: 43px; height: 3px; background: var(--bronze); margin-right: 13px;
  }
  .contact-item--title { font-weight: 700; letter-spacing: 2px; }
  .contact-item .sep { color: var(--bronze); margin: 0 6px; }
  .social-mark {
    width: 28px; height: 28px; border: 3px solid var(--bronze); margin-right: 13px; flex: none;
  }
  .social-mark--square { border-radius: 4px; }
  .social-mark--circle { border-radius: 50%; }
  .follow-note {
    position: absolute; left: 56px; top: 415px;
    font-family: "Bodoni Moda", serif; font-size: 11.5px; letter-spacing: 0.8px; color: var(--ink);
  }
  .owner-portrait {
    position: absolute; left: 186px; top: 491px; width: 120px; height: 120px;
    background: linear-gradient(160deg, var(--bronze-soft), var(--bronze-deep));
  }
  .owner-quote {
    position: absolute; left: 0; top: 640px; width: 500px; text-align: center;
    font-family: "Bodoni Moda", serif; font-size: 15px; line-height: 28px;
    letter-spacing: 1.2px; color: var(--bronze-soft);
  }
  .lash-ornament {
    position: absolute; left: 226px; top: 722px; width: 46px; height: 28px;
    background: var(--bronze-tint); border-radius: 14px;
  }
  .closing-rule { position: absolute; left: 100px; top: 786px; }
</style>
</head>
<body>
<div class="canvas">
  <section class="card card--front">
    <div class="eye-illustration" role="img" aria-label="Line drawing of a closed eye with long lashes in bronze"></div>
    <div class="front-wordmark">Lumarra</div>
    <div class="front-locale">BEVERLY HILLS</div>
    <div class="front-tagline">Personalized Eyelash Extensions</div>
  </section>

  <section class="card card--back">
    <div class="back-wordmark">Lumarra</div>
    <div class="back-locale">BEVERLY HILLS</div>

    <ul class="contact-list">
      <li class="contact-item contact-item--title" style="top:0">Lumarra<span class="sep">›</span>Personalized Eyelash Extensions</li>
      <li class="contact-item" style="top:37px">Mara Lindqvist</li>
      <li class="contact-item" style="top:73px">6128 N.Corbel Ridge Blvd Beverly Hills, CA 90210</li>
      <li class="contact-item" style="top:110px">310 555 01927(text only)</li>
      <li class="contact-item" style="top:147px">www.lumarrastudio-example.com</li>
      <li class="contact-item" style="top:183px"><span class="social-mark social-mark--square" aria-hidden="true"></span>@stylebymika</li>
      <li class="contact-item" style="top:219px"><span class="social-mark social-mark--circle" aria-hidden="true"></span>@lumarrastudioexample</li>
    </ul>
    <p class="follow-note">(follow us for seasonal campaigns and news @lumarrastudioexample)</p>

    <div class="owner-portrait" role="img" aria-label="Portrait of the salon owner in bronze tones"></div>
    <p class="owner-quote">"I care about each client as much as I care about<br>each individual lash." - Mika (owner)</p>
    <div class="lash-ornament" role="img" aria-label="Small lash motif"></div>

    <svg class="closing-rule" width="294" height="4" viewBox="0 0 294 4" aria-hidden="true">
      <defs>
        <linearGradient id="rule-gradient" x1="0" x2="1">
          <stop offset="0" stop-color="#a8895a"/>
          <stop offset="0.5" stop-color="#e9cd7e"/>
          <stop offset="1" stop-color="#a8895a"/>
        </linearGradient>
      </defs>
      <rect width="294" height="3" fill="url(#rule-gradient)"/>
    </svg>
  </section>
</div>
</body>
</html>
```